Web Design Project

site will be : www.chatbridgenow.example
We are a new business specialising in providing online customer support and sales services for a wide range of business types.

Will have to source suitable stock shots for images.
will also souce sample graphics of service, to follow.
Updates

Project Deadline Extended
Reason: This should allow enough time for any outstanding designs to be submitted. We are keen to press on so Further extension will only be considered if the designer contacts me with a very good reason.

Target Market(s)

Online Businesses

Industry/Entity Type

Business

Requirements
Must have
• Quick Assist Button....see briefing document for further details

```html
<!DOCTYPE html>
<html lang="en">
<head>
<meta charset="utf-8">
<title>Quick Assist Express</title>
<link rel="stylesheet" href="https://fonts.googleapis.com/css2?family=Arimo:wght@400;700&family=Gelasio:wght@400;700&display=swap">
<style>
:root{
  --sky-top:#0a6fd6;
  --sky-mid:#3a9ae8;
  --sky-low:#bfe0f6;
  --navy:#003a6b;
  --heading:#0d3a66;
  --accent:#2e9be6;
  --panel-grey:#e6e6e4;
  --frame-grey:#c9c9c9;
  --body-grey:#6d6d6d;
  --ink:#111;
  --white:#fff;
  --nav-top:#8fd3fb;
  --nav-bottom:#3aa9ea;
}
*{margin:0;padding:0;box-sizing:border-box}
html,body{width:1200px;height:964px;overflow:hidden}
body{
  position:relative;
  background:linear-gradient(180deg,var(--sky-top) 0,var(--sky-mid) 170px,var(--sky-low) 330px,#eef6fb 430px,var(--white) 520px);
  font-family:"Gelasio",Georgia,serif;
  color:var(--ink);
}
.top-rule{position:absolute;left:0;top:0;width:1200px;height:5px;background:var(--navy)}
.brand{
  position:absolute;left:77px;top:88px;width:300px;
  font-family:"Arimo",Arial,sans-serif;font-weight:700;font-size:27px;line-height:32px;
  color:var(--white);white-space:nowrap;
}
.tagline{
  position:absolute;left:434px;top:80px;
  font-family:"Arimo",Arial,sans-serif;font-weight:700;font-size:28px;line-height:32px;
  color:var(--white);white-space:nowrap;
}
.headset{
  position:absolute;left:1015px;top:53px;width:98px;height:98px;border-radius:50%;
  background:radial-gradient(circle at 40% 40%,#d9dde0,#6c7276 60%,#2c3033);
}
.ribbon{position:absolute;left:0;top:184px;width:1200px;height:70px}
.nav{
  position:absolute;left:67px;top:184px;width:1062px;height:47px;
  display:flex;list-style:none;
  background:linear-gradient(180deg,var(--nav-top),var(--nav-bottom));
  border-radius:6px 6px 0 0;
}
.nav li{
  display:flex;align-items:center;justify-content:center;
  font-size:18px;color:var(--ink);border-right:1px solid #2a8fd0;
}
.nav li:last-child{border-right:0}
.nav li.is-current{color:var(--white)}
.content{
  position:absolute;left:82px;top:231px;width:1035px;height:650px;
  background:var(--white);border:1px solid var(--frame-grey);border-top:0;
}
.hero-frame{
  position:absolute;left:13px;top:15px;width:1010px;height:332px;
  border:1px solid #d4d4d4;
}
.hero{
  position:absolute;left:6px;top:6px;width:997px;height:318px;background:var(--panel-grey);
}
.welcome{
  position:absolute;left:11px;top:18px;width:525px;
  font-size:20px;font-weight:400;color:var(--ink);white-space:nowrap;
}
.welcome strong{font-weight:400;font-size:28px;color:var(--heading);margin-left:4px}
.ask{
  position:absolute;left:16px;top:77px;width:525px;height:46px;
  background:linear-gradient(180deg,#f4f4f2,var(--panel-grey));
  font-size:22px;padding:14px 0 0 9px;
}
.needs{position:absolute;left:36px;top:137px;list-style:none}
.needs li{font-size:21px;color:var(--heading);height:36px;padding-left:20px;position:relative}
.needs li::before{
  content:"";position:absolute;left:0;top:8px;
  border-left:7px solid var(--heading);border-top:6px solid transparent;border-bottom:6px solid transparent;
}
.cta{position:absolute;left:25px;top:234px;font-size:22px;line-height:30px;color:var(--ink)}
.cta span{color:var(--accent)}
.photo-card{
  position:absolute;left:545px;top:8px;width:444px;height:302px;background:var(--white);padding:5px;
}
.photo{
  width:434px;height:247px;
  background:linear-gradient(100deg,#a8a8a2 0%,#d8cdb8 35%,#c9a48c 60%,#efe6dd 100%);
}
.photo-caption{
  height:45px;background:var(--navy);color:var(--white);
  font-family:"Arimo",Arial,sans-serif;font-weight:700;font-size:20px;
  display:flex;align-items:center;justify-content:center;white-space:nowrap;
}
.benefits-title{position:absolute;left:18px;top:360px;font-size:23px;color:var(--heading);font-weight:400}
.benefits-rule{position:absolute;left:18px;top:399px;width:999px;border-top:1px dotted #9a9a9a}
.benefits{position:absolute;left:22px;top:415px;list-style:none}
.benefits li{
  font-family:"Arimo",Arial,sans-serif;font-size:14px;color:var(--body-grey);
  height:28px;padding-left:18px;position:relative;
}
.benefits li::before{
  content:"";position:absolute;left:2px;top:4px;
  border-left:5px solid var(--navy);border-top:4px solid transparent;border-bottom:4px solid transparent;
}
.footer{
  position:absolute;left:0;top:894px;width:1200px;height:70px;background:var(--navy);
  border-top:3px solid #1d5d92;
  font-family:"Arimo",Arial,sans-serif;font-size:13px;color:var(--white);
  display:flex;align-items:center;justify-content:center;
}
</style>
</head>
<body>
<div class="top-rule"></div>
<div class="brand">Quick Assist Express</div>
<p class="tagline">Based in Ireland with European Agents to<br>Cater for a&nbsp; European Market</p>
<div class="headset" role="img" aria-label="Headset with microphone"></div>

<svg class="ribbon" viewBox="0 0 1200 70" aria-hidden="true">
  <path d="M14 24 Q45 12 82 20 L82 64 Q50 56 24 66 Q40 46 14 24Z" fill="#4fb2ea"/>
  <path d="M1119 20 Q1155 12 1190 24 Q1162 46 1178 66 Q1150 56 1119 64Z" fill="#4fb2ea"/>
</svg>
<ul class="nav">
  <li class="is-current" style="width:153px">Home</li>
  <li style="width:190px">Services</li>
  <li style="width:202px">About Us</li>
  <li style="width:160px">FAQ</li>
  <li style="width:181px">Pricing</li>
  <li style="width:176px">Contact Us</li>
</ul>

<main class="content">
  <section class="hero-frame">
    <div class="hero">
      <h1 class="welcome">Welcome to <strong>QUICK ASSIST EXPRESS</strong></h1>
      <div class="ask">DO YOU</div>
      <ul class="needs">
        <li>Need to close more online sales ?</li>
        <li>Want to improve your customer support ?</li>
      </ul>
      <p class="cta">GET <span>LIVE CHAT CUSTOMER HELP</span> ON YOUR<br>WEBSITE TODAY !</p>
      <div class="photo-card">
        <div class="photo" role="img" aria-label="Photo of smiling support agents wearing headsets"></div>
        <div class="photo-caption">WE CAN BRING YOUR WEBSITE TO LIFE</div>
      </div>
    </div>
  </section>
  <h2 class="benefits-title">Quick Assist Express will :</h2>
  <div class="benefits-rule"></div>
  <ul class="benefits">
    <li>Convert visitors to your website into customers</li>
    <li>Improve Customer Communication</li>
    <li>Monitor visitors to your website in real time</li>
    <li>Work closely with you to identify your support requirements</li>
    <li>Provide professional agents to implement those requirements</li>
    <li>Reduce your operational costs</li>
    <li>Provide detailed website traffic reports</li>
  </ul>
</main>

<footer class="footer">© 2011, All Rights Reserved</footer>
</body>
</html>
```